Wireframes of In Store Preview

We need to simplify our in store preview capability. For this particular project what I really need are wireframes for the in store preview form, which is currently several pages - but needs to be condensed. The current Free In-Store Preview process is divided over five pages and is closely tied to the process of purchasing a product. This project simplifies the process and highlights the “no obligation to buy” value proposition of the feature.
Objectives
Simplify the Free In Store Preview (FISP) reservation process. We believe that reducing the number of pages required to complete the reservation process will reduce abandonment. Currently there is a 80+% drop off between the FISP - Edit page and the FISP - Review page. Some of this is to be expected, but we feel that if we can do the following that we can reduce some of that drop-off:
1. highlight the “no obligation to buy” and “see it in person” aspects of FISP
2. Remove the Veltmore Lending option from the payment method form - the CC is only needed to secure the reservation, so having this option here implies that this method is the final form of payment. During the final purchase the customer can choose to use Financing instead.
3. Remove selection of Protection Plan, deferring that to the post-reservation sale, which can provide a better hands-on, concierge experience.
4. reduce the steps from 5 steps to 2.
Here is the current flow:
1. Click Free In Store Preview on the PDP
2. A pop-up displays with the ring size and insurance option - the customer has to choose to preview it again 😔 Edit, Review and then Thank you) to 2 steps (edit/review and then thank you)
3. the form is displayed with the store location and credit card information
4. the review page is displayed on which the customer needs to finalize
5. the thank you page displays
Here is the new flow I’d like to get wireframes for:
* Click Free In Store Preview on the PDP (I don’t need a wireframe for this)
* the form is displayed with the store location and credit card form - once the customer enters their information they can finalize the reservation
* the thank you page displays
I’ve included screenshots of the current flow here. Also - FYI - as an example, I think Dunsel Oakes does a good job of communicating that their Desk Sample Kit option is free even though they do require a credit card authorization to complete the transaction. Also, their core user base is Millenial - just like ours. (I know, you wouldn't know it from our current website! :-) Anyway - I like their cleaner more tech saavy form behavior. So, don't be shy about moving away from the overcrowded multi-step form pages we have now.
Lastly - if you want to try the flow yourself - you can follow these steps:
1. Click here: https://www.bravelle-example.com/engagement-rings/solitaire-diamond-gallery-engagement-ring-in-14kt-white-gold/19815
2. On the setting PDP page here - click the CHOOSE THIS RING button.
3. That will take you to the diamond inventory where you need to select a diamond. Choose any diamond and “add it to your engagement ring” - this will take you to the configured ring PDP
4. Click the FREE IN STORE PREVIEW option on the configured ring PDP - a pop up will display
5. On the pop up, select the ring size (I know, I know - even if you selected one before you’ll need to select it again, this is a bug) and then click the PREVIEW THIS RING button. This will take you to the Free-in-store preview page form.
6. On the free in store preview page, enter a credit card payment method and hit the CONTINUE button. I promise - your card will NOT be charged if you hit this button. This will take you to the Review page.
7. On the Review Page you should STOP. PLEASE DO NOT PROCEED PAST THIS POINT. Please refer to the comp for the thank you page.
Thanks!
Target Market(s)
Millenial Engagement Ring Shoppers
Industry/Entity Type
Store
Number of Pages Required
2 page
Look and feel
Each slider illustrates characteristics of the customer's brand and the style your logo design should communicate.

```html
<!DOCTYPE html>
<html lang="en">
<head>
<meta charset="utf-8">
<title>Bravelle – Free In Store Preview</title>
<link rel="stylesheet" href="https://fonts.googleapis.com/css2?family=Mulish:wght@400;600;700;800&display=swap">
<style>
  :root {
    --plum: #6b1f45;
    --plum-line: #8a4a6a;
    --ink: #3d3d3d;
    --muted: #6a6a6a;
    --gold: #e0a800;
    --logo-gold: #e8b21c;
    --spinner: #ec4f8f;
    --card-blue: #2a4a9a;
    --bg: #ffffff;
    --ring-light: #f2f3f5;
    --ring-dark: #9aa0a8;
  }
  * { box-sizing: border-box; margin: 0; padding: 0; }
  html, body { width: 1200px; height: 2635px; overflow: hidden; background: var(--bg); }
  body { font-family: "Mulish", Arial, sans-serif; color: var(--ink); position: relative; }
  .abs { position: absolute; }
  .c { transform: translate(-50%, -50%); white-space: nowrap; }
  .l { transform: translateY(-50%); white-space: nowrap; }
  .r { transform: translate(-100%, -50%); white-space: nowrap; }

  .header-phone { left: 195px; top: 80px; font-size: 12px; font-weight: 800; color: var(--muted); }
  .brand { left: 600px; top: 80px; display: flex; align-items: center; gap: 10px; }
  .brand-dot { width: 36px; height: 36px; border-radius: 50%; background: var(--logo-gold); }
  .brand-name { font-size: 34px; font-weight: 800; letter-spacing: 3px; color: var(--ink); }
  .header-account { left: 960px; top: 80px; font-size: 12px; font-weight: 600; color: var(--muted); }

  .product-photo { background: radial-gradient(ellipse at center, var(--ring-light) 35%, var(--ring-dark) 100%); border-radius: 50%; }
  .product-photo.small { left: 548px; top: 188px; width: 112px; height: 50px; }
  .product-name { left: 600px; top: 263px; font-size: 12px; font-weight: 800; color: var(--plum); }
  .page-title { left: 600px; top: 306px; font-size: 31px; font-weight: 600; color: var(--plum); }

  .field { height: 2px; background: var(--plum-line); }
  .field-label { font-size: 20px; color: var(--ink); }

  .cc-note { left: 367px; top: 800px; font-size: 18px; line-height: 26px; color: var(--muted); }

  .spinner { width: 28px; height: 28px; }

  .detail-label { font-size: 17px; font-weight: 600; color: var(--ink); }
  .detail-text { font-size: 17px; color: var(--ink); }
  .card-chip { left: 588px; top: 1038px; width: 47px; height: 30px; border: 2px solid #c9cdd6; border-radius: 3px; background: #fff; }
  .card-chip::after { content: ""; position: absolute; left: 8px; right: 8px; top: 10px; height: 7px; background: var(--card-blue); }
  .more-link { font-size: 15px; font-weight: 800; color: var(--gold); }
  .edit-icon { width: 16px; height: 16px; }

  .btn-outline { border: 2px solid var(--plum-line); display: flex; align-items: center; justify-content: center; color: var(--plum); font-weight: 800; }
  .btn-see { left: 492px; top: 1241px; width: 209px; height: 53px; font-size: 18px; }
  .btn-note { left: 590px; top: 1315px; font-size: 15px; font-weight: 600; color: var(--ink); }

  .product-photo.large { left: 370px; top: 1606px; width: 184px; height: 78px; }
  .store-address { left: 612px; top: 1612px; font-size: 15px; font-weight: 800; line-height: 21px; color: var(--muted); }
  .window-label { left: 389px; top: 1745px; font-size: 17px; font-weight: 700; color: var(--ink); }
  .window-dates { left: 670px; top: 1743px; font-size: 25px; font-weight: 800; color: var(--ink); }

  .summary { left: 345px; top: 1825px; width: 545px; height: 184px; border: 2px solid var(--plum-line); }
  .summary-label { left: 377px; font-size: 17px; font-weight: 700; color: var(--ink); }
  .summary-value { left: 835px; font-size: 17px; font-weight: 600; color: var(--ink); }

  .btn-complete { left: 442px; top: 2083px; width: 353px; height: 76px; font-size: 26px; border-width: 3px; }
  .promise { left: 605px; top: 2210px; font-size: 25px; line-height: 32px; color: var(--plum); text-align: center; }
  .promise strong { font-weight: 800; }

  .footer-links { left: 610px; top: 2457px; font-size: 17px; color: var(--ink); }
  .footer-links span { margin: 0 10px; }
  .copyright { left: 608px; top: 2489px; font-size: 15px; color: var(--ink); }
  .footer-dot { left: 595px; top: 2553px; width: 38px; height: 38px; border-radius: 50%; background: var(--logo-gold); transform: translate(-50%, -50%); }
</style>
</head>
<body>

<header>
  <div class="abs l header-phone">1.888.555.0142</div>
  <div class="abs c brand"><span class="brand-dot"></span><span class="brand-name">BRAVELLE</span></div>
  <div class="abs l header-account">MY ACCOUNT</div>
</header>

<main>
  <div class="abs product-photo small" role="img" aria-label="Solitaire diamond engagement ring photo"></div>
  <div class="abs c product-name">SOLITAIRE DIAMOND GALLERY ENGAGEMENT RING</div>
  <h1 class="abs c page-title">FREE IN STORE PREVIEW</h1>

  <!-- Contact & address form -->
  <div class="abs l field-label" style="left:373px;top:405px">First Name</div>
  <div class="abs field" style="left:360px;top:414px;width:224px"></div>
  <div class="abs l field-label" style="left:602px;top:405px">Last Name</div>
  <div class="abs field" style="left:591px;top:414px;width:235px"></div>

  <div class="abs l field-label" style="left:372px;top:488px">Email</div>
  <div class="abs field" style="left:360px;top:514px;width:260px"></div>
  <div class="abs l field-label" style="left:639px;top:488px">Contact Phone</div>
  <div class="abs field" style="left:627px;top:514px;width:199px"></div>

  <div class="abs l field-label" style="left:371px;top:575px">Street Address</div>
  <div class="abs field" style="left:362px;top:601px;width:466px"></div>

  <div class="abs l field-label" style="left:374px;top:666px">State</div>
  <div class="abs field" style="left:360px;top:682px;width:134px"></div>
  <div class="abs l field-label" style="left:515px;top:665px">City</div>
  <div class="abs field" style="left:499px;top:682px;width:175px"></div>
  <div class="abs l field-label" style="left:722px;top:665px">Zip</div>
  <div class="abs field" style="left:679px;top:682px;width:147px"></div>

  <!-- Card form -->
  <div class="abs l field-label" style="left:376px;top:783px">Credit Card No.</div>
  <div class="abs l field-label" style="left:638px;top:781px">CCV</div>
  <div class="abs l field-label" style="left:758px;top:779px">MM/YY</div>
  <div class="abs field" style="left:360px;top:799px;width:466px"></div>

  <p class="abs cc-note">The CC&nbsp; information is needed to secure your reservation.<br>No charges would be made for your in-store preview.</p>

  <svg class="abs c spinner" style="left:602px;top:964px" viewBox="0 0 28 28" aria-hidden="true">
    <path d="M14 3 A11 11 0 1 1 3.5 10.5" fill="none" stroke="var(--spinner)" stroke-width="3" stroke-linecap="round"/>
  </svg>

  <!-- Saved details -->
  <div class="abs l detail-label" style="left:394px;top:1059px">CARD DETAILS</div>
  <div class="abs card-chip" aria-label="Card"></div>
  <div class="abs l detail-text" style="left:653px;top:1051px">•••• •• 1911</div>
  <svg class="abs edit-icon" style="left:743px;top:1003px;top:1004px" viewBox="0 0 16 16" aria-hidden="true"><path d="M2 14 L3 10 L11 2 L14 5 L6 13 Z" fill="var(--gold)"/></svg>

  <div class="abs l detail-label" style="left:394px;top:1121px">BILLING DETAILS</div>
  <div class="abs l detail-text" style="left:582px;top:1105px">Owen Marsh</div>
  <div class="abs l detail-text" style="left:582px;top:1133px">14 Alder Lane</div>
  <div class="abs l more-link" style="left:582px;top:1162px">more</div>
  <svg class="abs edit-icon" style="left:743px;top:1093px" viewBox="0 0 16 16" aria-hidden="true"><path d="M2 14 L3 10 L11 2 L14 5 L6 13 Z" fill="var(--gold)"/></svg>

  <div class="abs btn-outline btn-see">SEE RING IN PERSON</div>
  <div class="abs c btn-note">THE PREVIEW IS FREE</div>

  <svg class="abs c spinner" style="left:602px;top:1452px" viewBox="0 0 28 28" aria-hidden="true">
    <path d="M14 3 A11 11 0 1 1 3.5 10.5" fill="none" stroke="var(--spinner)" stroke-width="3" stroke-linecap="round"/>
  </svg>

  <!-- Confirmation -->
  <h2 class="abs c page-title" style="top:1535px">SEE IT IN PERSON</h2>
  <div class="abs product-photo large" role="img" aria-label="Solitaire diamond engagement ring photo"></div>
  <address class="abs store-address" style="font-style:normal">MAREN HOLT FINE JEWELERS<br>30, Lorem Avenue, Ipsum Way,<br>Los Angeles LA90908</address>

  <div class="abs l window-label">PREVIEW YOUR RING BETWEEN</div>
  <div class="abs l window-dates">Sept 1 - Sept 7</div>

  <div class="abs summary"></div>
  <div class="abs l summary-label" style="top:1874px">ORDER PRICE</div>
  <div class="abs r summary-value" style="top:1876px">$ 3209</div>
  <div class="abs l summary-label" style="top:1915px;left:379px">PREVIEW FREE</div>
  <div class="abs r summary-value" style="top:1913px;left:823px">$ 0</div>
  <div class="abs l summary-label" style="top:1955px;left:380px">AMOUNT CHARGED</div>
  <div class="abs r summary-value" style="top:1957px;left:832px">$ 0.00</div>

  <div class="abs btn-outline btn-complete">COMPLETE RESERVATION</div>
  <p class="abs c promise">You reservation is free and you are under<br><strong>no obligation to buy</strong> the item</p>
</main>

<footer>
  <div class="abs c footer-links">Privacy policy<span>|</span>Terms<span>|</span>Financing</div>
  <div class="abs c copyright">C 2017. All rights Reserved</div>
  <div class="abs footer-dot"></div>
</footer>

</body>
</html>
```